lawn service business card design

i want a front yard landscape with street sign visable which says "Pelbrook Ave". the logo on the card says "the lawns of Pelbrook Ave" by Curtis Vandermolen (555) 318-0964
i also want matching address labels and letter head.

Industry/Entity Type

Landscape

Contact Information for Business Card

Requirements
Must have
• i want a front yard landscape with street sign visable which says "Pelbrook Ave". the logo on the card says "the lawns of Pelbrook Ave" by Curtis Vandermolen (555) 318-0964

```html
<!DOCTYPE html>
<html lang="en">
<head>
<meta charset="utf-8">
<title>The Lawns of Pelbrook Ave – Stationery</title>
<link rel="stylesheet" href="https://fonts.googleapis.com/css2?family=Cinzel:wght@400&family=Poppins:wght@400;500&display=swap">
<style>
  :root {
    --backdrop: #ababab;
    --paper: #ffffff;
    --green-light: #55a048;
    --green-dark: #1d5a2b;
    --ink-green: #1f5a2a;
    --silver-dark: #6e6e6e;
    --silver-light: #f4f4f4;
    --logo-ink: #ffffff;
  }
  * { margin: 0; padding: 0; box-sizing: border-box; }
  html, body {
    width: 1200px;
    height: 900px;
    overflow: hidden;
    background: var(--backdrop);
    font-family: "Poppins", sans-serif;
  }
  .canvas { position: relative; width: 1200px; height: 900px; }

  .sheet { position: absolute; background: var(--paper); }

  .rule {
    position: absolute;
    left: 0; right: 0;
    height: 4px;
    background: linear-gradient(90deg, var(--silver-dark), var(--silver-light) 50%, var(--silver-dark));
  }
  .band {
    position: absolute;
    left: 0; right: 0;
    background: linear-gradient(180deg, var(--green-light), var(--green-dark));
    display: flex;
    flex-direction: column;
    align-items: center;
    justify-content: center;
  }
  .brand-name {
    font-family: "Cinzel", serif;
    color: var(--logo-ink);
    font-weight: 400;
    text-transform: uppercase;
    text-align: center;
    line-height: 1;
    white-space: nowrap;
  }
  .brand-name span { display: block; }

  /* Address label */
  .address-label { left: 28px; top: 290px; width: 516px; height: 174px; }
  .address-label .rule-top { top: 17px; }
  .address-label .band { top: 21px; height: 81px; }
  .address-label .rule-bottom { top: 102px; }
  .address-label .brand-name { font-size: 34px; letter-spacing: 0.01em; }
  .address-label .brand-name span + span { margin-top: 4px; }
  .label-contact {
    position: absolute;
    top: 110px; left: 0; right: 0;
    text-align: center;
    color: var(--ink-green);
    white-space: nowrap;
  }
  .label-contact .person { font-size: 19px; font-weight: 500; line-height: 26px; }
  .label-contact .street { font-size: 19px; font-weight: 400; line-height: 25px; letter-spacing: 0.2px; }

  /* Letterhead */
  .letterhead { left: 573px; top: 42px; width: 572px; height: 810px; }
  .letterhead .rule-top { top: 26px; }
  .letterhead .band { top: 30px; height: 76px; }
  .letterhead .rule-bottom { top: 106px; }
  .letterhead .brand-name { font-size: 31px; }
  .letterhead .brand-name span + span { margin-top: 3px; }
  .letter-footer {
    position: absolute;
    left: 26px; top: 740px;
    color: var(--ink-green);
    font-style: normal;
    font-size: 13px;
    line-height: 16.5px;
    white-space: nowrap;
  }
  .letter-footer .person { font-weight: 500; }
</style>
</head>
<body>
  <main class="canvas">
    <section class="sheet address-label" aria-label="Address label">
      <div class="rule rule-top"></div>
      <div class="band">
        <p class="brand-name"><span>The Lawns of</span><span>Pelbrook Ave</span></p>
      </div>
      <div class="rule rule-bottom"></div>
      <div class="label-contact">
        <p class="person">Curtis Vandermolen</p>
        <p class="street">4170 NW 18th st OKC OK 73190</p>
      </div>
    </section>

    <section class="sheet letterhead" aria-label="Letterhead">
      <div class="rule rule-top"></div>
      <div class="band">
        <p class="brand-name"><span>The Lawns of</span><span>Pelbrook Ave</span></p>
      </div>
      <div class="rule rule-bottom"></div>
      <address class="letter-footer">
        <p class="person">Curtis Vandermolen</p>
        <p>(555) 318-0964</p>
        <p>4170 NW 18th st OKC OK 73190</p>
      </address>
    </section>
  </main>
</body>
</html>
```